Website Design for a holiday home letting busines

We require a redesign of our present website www.fernbrookstays.com. We want the website to stand out and look professional and clean to make holiday hunters want to book a caravan or lodge holiday with us. Our logo is red however we DO NOT want the website to be red. We want a natural colour scheme.

The final design should communicate that we are a professional company to book with.

On the home page we require;
Overview of company
Photo
Search box for holiday (check in)
Late Deals
Reviews
News

We would like the following pages designed; home page, available dates page, caravans page, content page.

The website should be responsive for smart phones. One website I do like is http://www.brimoveld.be/nl/

Target Market(s)

Families

Industry/Entity Type

Travel

Number of Pages Required

5+ page

Font styles to use
Serif

Requirements
Must have
• The project must be responsive for mobile phones and tablets.
• Ability to search for holiday home holidays
• We want a natural colour scheme.
Nice to have
• A style we like is http://www.brimoveld.be/nl/
Should not have
• Do not use red as a colour for the website. Our logo is red so this is the only time we want this used.

```html
<!DOCTYPE html>
<html lang="en">
<head>
<meta charset="utf-8">
<title>Fernbrook Stays – Private Holiday Rentals</title>
<link href="https://fonts.googleapis.com/css2?family=Ubuntu:wght@400;500;700&family=Open+Sans:wght@400;600;700&display=swap" rel="stylesheet">
<style>
:root{
  --blue:#1b7cc3;
  --blue-dark:#125c96;
  --green:#8db42b;
  --green-dark:#6f9420;
  --ink:#333;
  --muted:#8a8a8a;
  --line:#e3e3e3;
  --paper:#ffffff;
  --soft:#f3f3f3;
  --dark:#262a2e;
  --star:#e8a41c;
}
*{box-sizing:border-box;margin:0;padding:0}
html,body{width:1200px;height:3964px;overflow:hidden}
body{font-family:"Open Sans",Arial,sans-serif;color:var(--ink);background:var(--paper);font-size:13px;position:relative}
h1,h2,h3,h4{font-family:"Ubuntu",Arial,sans-serif;font-weight:500}
.wrap{width:1008px;margin:0 auto;position:relative}

/* header */
.site-header{height:144px;border-bottom:1px solid var(--line)}
.site-header .wrap{height:144px;display:flex;align-items:center;justify-content:space-between}
.brand{display:flex;align-items:center;gap:14px}
.brand-dot{width:44px;height:44px;border-radius:50%;background:var(--blue)}
.brand-name{font-family:"Ubuntu",sans-serif;font-size:30px;font-weight:500;color:var(--blue)}
.header-right{display:flex;align-items:center;gap:22px}
.call{font-size:11px;color:var(--muted);line-height:1.3}
.call strong{display:block;font-size:19px;color:var(--ink)}
.help{display:flex;align-items:center;gap:8px}
.help-avatar{width:40px;height:40px;border-radius:50%;background:#c9d3dc}
.help-tag{background:var(--green);color:#fff;font-size:12px;padding:6px 10px;border-radius:3px;font-weight:600}
.year-btns{display:flex;gap:8px}
.year-btn{padding:10px 18px;border-radius:20px;color:#fff;font-weight:700;font-size:15px;font-family:"Ubuntu",sans-serif}
.year-btn.grey{background:#7d858c}
.year-btn.blue{background:var(--blue)}

.main-nav{height:48px;border-bottom:1px solid var(--line)}
.main-nav ul{list-style:none;display:flex;gap:34px;height:48px;align-items:center;font-size:12px;font-weight:600;color:#666;text-transform:uppercase}
.main-nav li.active{color:var(--blue);border-bottom:3px solid var(--blue);padding-bottom:12px;margin-top:15px}

/* hero */
.hero{position:relative;height:588px}
.hero-photo{position:absolute;inset:0;background:linear-gradient(180deg,#9fc3de 0%,#c9dbe6 38%,#6e8ea6 55%,#5a6a68 75%,#3d4a48 100%)}
.hero .wrap{height:588px}
.hero-title{position:absolute;left:0;top:48px}
.hero-title h1{font-size:40px;line-height:1.1;color:#fff;font-weight:700;text-shadow:0 1px 3px rgba(0,0,0,.25)}
.hero-title h1 span{color:var(--blue);display:block}
.hero-title p{margin-top:14px;background:var(--blue);color:#fff;font-size:12px;font-weight:600;padding:8px 12px;width:330px;line-height:1.4}
.checkin{position:absolute;right:0;top:36px;width:448px;background:rgba(255,255,255,.9);padding:20px 24px 24px;border-radius:3px}
.checkin h2{font-size:30px;color:var(--ink);margin-bottom:14px}
.field{background:var(--blue);color:#dbeaf6;font-size:12px;height:38px;border-radius:3px;display:flex;align-items:center;justify-content:space-between;padding:0 12px;margin-bottom:10px}
.field-row{display:flex;gap:10px}
.field-row .field{flex:1}
.search-btn{background:var(--blue-dark);color:#fff;height:40px;border-radius:3px;display:flex;align-items:center;justify-content:center;font-weight:700;font-size:14px}

/* intro */
.intro{padding:60px 0 50px}
.intro .wrap{display:flex;gap:24px;height:380px}
.slider{flex:0 0 492px;background:var(--dark);position:relative;color:#fff;overflow:hidden}
.slider-photo{position:absolute;inset:0;background:linear-gradient(135deg,#3b4650,#1d2226)}
.slider-body{position:absolute;left:28px;top:28px;width:430px}
.slider-body h3{font-size:22px;font-weight:700;margin-bottom:14px}
.slider-body h3 span{color:var(--green)}
.slider-body p{font-size:12px;line-height:1.7;color:#d6d6d6}
.slider-nav{position:absolute;bottom:22px;left:0;right:0;display:flex;justify-content:space-between;align-items:center;padding:0 20px}
.dots{display:flex;gap:8px}
.dots i{width:8px;height:8px;border-radius:50%;background:#777;display:block}
.dots i.on{background:#fff}
.intro-right{flex:1;display:flex;flex-direction:column;gap:12px}
.welcome{background:var(--blue);color:#fff;padding:40px 40px;flex:0 0 200px}
.welcome h2{font-size:36px;line-height:1.2;font-weight:500}
.reviews{background:var(--green);color:#fff;padding:28px 40px;flex:1;position:relative}
.reviews h2{font-size:34px;margin-bottom:12px}
.reviews p{font-size:12px;line-height:1.6;width:360px}
.reviews .dots{position:absolute;left:40px;bottom:20px}
.reviews .dots i{background:rgba(255,255,255,.5)}
.reviews .dots i.on{background:#fff}
.reviews .arr{position:absolute;right:24px;bottom:14px}

/* section headings */
.sec-title{text-align:center;font-size:30px;color:var(--ink);font-weight:500;text-transform:uppercase;margin-bottom:30px}

/* property cards */
.lodges{padding:40px 0 40px;border-top:1px solid var(--line)}
.card-grid{display:grid;grid-template-columns:repeat(4,252px);grid-auto-rows:232px;border:1px solid var(--line)}
.ph{display:block}
.card-text{padding:22px 20px;position:relative;background:#fff}
.card-text h3{font-size:19px;color:var(--ink);text-transform:uppercase;margin-bottom:6px}
.card-text .rule{width:80%;height:1px;background:var(--line);margin:6px 0 12px}
.card-text p{font-size:11px;color:var(--muted);line-height:1.6}
.card-foot{position:absolute;left:20px;right:20px;bottom:22px;display:flex;justify-content:space-between;align-items:center}
.more{background:var(--green);color:#fff;font-size:10px;padding:4px 9px;border-radius:2px}
.stars{color:var(--star);font-size:13px;letter-spacing:1px}
.view-all{display:block;width:150px;margin:34px auto 0;background:var(--blue);color:#fff;text-align:center;border-radius:22px;padding:12px 0;font-weight:700;font-size:13px}

/* late deals */
.deals{position:relative;height:396px}
.deals-bg{position:absolute;inset:0;background:linear-gradient(180deg,#2c3035,#3e4449)}
.deals .wrap{padding-top:28px}
.deals .sec-title{color:#fff;margin-bottom:22px}
.deal-grid{display:grid;grid-template-columns:repeat(4,252px);grid-auto-rows:232px}

/* why book */
.why{padding:46px 0 50px}
.why-grid{display:grid;grid-template-columns:repeat(4,1fr);gap:30px;text-align:center}
.why-circle{width:200px;height:200px;border-radius:50%;border:6px solid var(--green);margin:0 auto 22px;display:flex;align-items:center;justify-content:center}
.why-circle.blue{border-color:var(--blue)}
.why-item h4{color:var(--green);font-size:17px;line-height:1.3;margin-bottom:12px;font-weight:700}
.why-item p{font-size:11px;color:var(--muted);line-height:1.6;width:200px;margin:0 auto}

/* things to do */
.things{padding:38px 0 40px;border-top:1px solid var(--line)}
.things-grid{display:grid;grid-template-columns:repeat(4,252px);grid-auto-rows:232px;gap:0}
.thing{display:flex;border:1px solid var(--line)}
.thing .ph{width:118px;flex:0 0 118px}
.thing .t{padding:12px 10px}
.thing h4{color:var(--green);font-size:17px;margin-bottom:6px;font-weight:700}
.thing p{font-size:10px;color:var(--muted);line-height:1.55}

/* footer */
.site-footer{position:absolute;left:0;right:0;top:3520px;height:400px;background:var(--blue);color:#fff}
.site-footer .wrap{display:flex;gap:40px;padding-top:44px}
.f-col h4{font-size:20px;font-weight:700;text-transform:uppercase;margin-bottom:20px}
.f-col p{font-size:11px;line-height:1.6;color:#d9e9f6}
.news{width:320px}
.input{background:#fff;color:#999;font-size:11px;height:30px;display:flex;align-items:center;padding:0 10px;margin-top:12px;border-radius:2px}
.subscribe{display:inline-block;background:var(--green);color:#fff;font-weight:700;font-size:12px;padding:9px 18px;margin-top:14px;border-radius:2px}
.contact{width:300px}
.contact li{list-style:none;display:flex;align-items:center;gap:10px;font-size:12px;margin-top:12px}
.sitemap{flex:1;padding-left:40px;border-left:1px solid rgba(255,255,255,.25)}
.sitemap ul{list-style:none;columns:2;font-size:12px;line-height:2.2;color:#e8f2fa}
.bottom-bar{position:absolute;left:0;right:0;top:3920px;height:44px;background:var(--blue-dark);color:#cfe2f2;font-size:11px}
.bottom-bar .wrap{display:flex;justify-content:space-between;align-items:center;height:44px}
.social{display:flex;align-items:center;gap:10px}
.social i{width:18px;height:18px;border-radius:50%;background:#fff;opacity:.85;display:block}
</style>
</head>
<body>

<header class="site-header">
  <div class="wrap">
    <div class="brand"><span class="brand-dot"></span><span class="brand-name">Fernbrook Stays</span></div>
    <div class="header-right">
      <div class="call">General enquiries<strong>0800 000 4821</strong></div>
      <div class="help"><span class="help-avatar" role="img" aria-label="Support agent portrait"></span><span class="help-tag">Questions? Live chat</span></div>
      <div class="year-btns"><span class="year-btn grey">2015 HOLIDAYS</span><span class="year-btn blue">2016 HOLIDAYS</span></div>
    </div>
  </div>
</header>

<nav class="main-nav">
  <div class="wrap">
    <ul>
      <li class="active">Home</li><li>News</li><li>Reviews</li><li>Caravans &amp; Lodges</li><li>Different Pods</li><li>Thornbeck Castle</li><li>Local Attractions</li><li>Contact Us</li>
    </ul>
  </div>
</nav>

<section class="hero">
  <div class="hero-photo" role="img" aria-label="Coastal road beside rocky shore under a bright sky"></div>
  <div class="wrap">
    <div class="hero-title">
      <h1>PRIVATE<span>HOLIDAY RENTALS</span></h1>
      <p>QUALITY LODGE &amp; CARAVAN HIRE AT THORNBECK CASTLE HOLIDAY PARK. BOOK ONLINE TODAY!</p>
    </div>
    <form class="checkin">
      <h2>CHECK IN</h2>
      <div class="field"><span>Where do you want to go</span>
        <svg width="12" height="14" viewBox="0 0 12 14"><path d="M6 0a5 5 0 0 0-5 5c0 4 5 9 5 9s5-5 5-9a5 5 0 0 0-5-5zm0 7a2 2 0 1 1 0-4 2 2 0 0 1 0 4z" fill="#fff"/></svg></div>
      <div class="field-row">
        <div class="field"><span>Check in</span><svg width="12" height="12"><rect x="1" y="2" width="10" height="9" fill="none" stroke="#fff"/><line x1="1" y1="5" x2="11" y2="5" stroke="#fff"/></svg></div>
        <div class="field"><span>Check out</span><svg width="12" height="12"><rect x="1" y="2" width="10" height="9" fill="none" stroke="#fff"/><line x1="1" y1="5" x2="11" y2="5" stroke="#fff"/></svg></div>
      </div>
      <div class="field"><span>Guests</span><svg width="12" height="12"><circle cx="6" cy="4" r="3" fill="#fff"/><path d="M0 12a6 5 0 0 1 12 0z" fill="#fff"/></svg></div>
      <div class="search-btn">Search</div>
    </form>
  </div>
</section>

<section class="intro">
  <div class="wrap">
    <div class="slider">
      <div class="slider-photo" role="img" aria-label="Dark holiday lodge interior"></div>
      <div class="slider-body">
        <h3>CONTRARY TO <span>POPULAR BELIEF</span></h3>
        <p>A holiday park stay need not be basic. Our privately owned lodges and caravans are cleaned, checked and ready for your arrival, with modern kitchens, comfy beds and space for the whole family to relax.</p>
      </div>
      <div class="slider-nav">
        <svg width="10" height="14"><path d="M8 1 2 7l6 6" stroke="#fff" stroke-width="2" fill="none"/></svg>
        <div class="dots"><i class="on"></i><i></i><i></i><i></i></div>
        <svg width="10" height="14"><path d="m2 1 6 6-6 6" stroke="#fff" stroke-width="2" fill="none"/></svg>
      </div>
    </div>
    <div class="intro-right">
      <div class="welcome"><h2>WELCOME TO<br>FERNBROOK STAYS</h2></div>
      <div class="reviews">
        <h2>REVIEWS</h2>
        <p>Lovely stay in a spotless caravan, the kids loved the pool and the park. We will definitely book again next summer.</p>
        <div class="dots"><i class="on"></i><i></i><i></i><i></i></div>
        <svg class="arr" width="34" height="14"><path d="M8 1 2 7l6 6M26 1l6 6-6 6" stroke="#fff" stroke-width="2" fill="none"/></svg>
      </div>
    </div>
  </div>
</section>

<section class="lodges">
  <div class="wrap">
    <h2 class="sec-title">Our Caravans and Lodges</h2>
    <div class="card-grid">
      <div class="ph" style="background:linear-gradient(135deg,#b89a78,#6d5a46)" role="img" aria-label="Caravan living room interior"></div>
      <div class="card-text"><h3>The Ashford</h3><div class="rule"></div><p>The Ashford has three bedrooms and a bright open plan lounge with sea views.</p><div class="card-foot"><span class="more">Read more</span><span class="stars">★★★★★</span></div></div>
      <div class="ph" style="background:linear-gradient(135deg,#c8b79c,#8a7559)" role="img" aria-label="Lodge lounge with sofas"></div>
      <div class="card-text"><h3>The Kestrel</h3><div class="rule"></div><p>The Kestrel sleeps six and comes with a decked terrace and outdoor seating.</p><div class="card-foot"><span class="more">Read more</span><span class="stars">★★★★★</span></div></div>
      <div class="card-text"><h3>The Alder</h3><div class="rule"></div><p>The Alder offers a modern kitchen and two bathrooms for larger families.</p><div class="card-foot"><span class="more">Read more</span><span class="stars">★★★★★</span></div></div>
      <div class="ph" style="background:linear-gradient(135deg,#d4c6b0,#9b876c)" role="img" aria-label="Caravan bedroom"></div>
      <div class="card-text"><h3>The Bramley</h3><div class="rule"></div><p>The Bramley is a cosy lodge close to the lake and the children's play area.</p><div class="card-foot"><span class="more">Read more</span><span class="stars">★★★★★</span></div></div>
      <div class="ph" style="background:linear-gradient(135deg,#a3b4c2,#5f6e7a)" role="img" aria-label="Lodge dining area"></div>
    </div>
    <span class="view-all">VIEW ALL</span>
  </div>
</section>

<section class="deals">
  <div class="deals-bg" role="img" aria-label="Dimmed holiday park landscape"></div>
  <div class="wrap">
    <h2 class="sec-title">Late Deals</h2>
    <div class="deal-grid">
      <div class="ph" style="background:linear-gradient(180deg,#a9c9e2,#8aa36a)" role="img" aria-label="Caravan on a sunny park pitch"></div>
      <div class="card-text"><h3>The Ashford</h3><div class="rule"></div><p>Seven nights from the 12th, now reduced for last minute bookings.</p><div class="card-foot"><span class="more">Read more</span><span class="stars">★★★★★</span></div></div>
      <div class="ph" style="background:linear-gradient(180deg,#7fa8cf,#c9a578)" role="img" aria-label="Family enjoying a holiday outdoors"></div>
      <div class="card-text"><h3>The Kestrel</h3><div class="rule"></div><p>Short break offer for four nights, available this weekend only.</p><div class="card-foot"><span class="more">Read more</span><span class="stars">★★★★★</span></div></div>
    </div>
  </div>
</section>

<section class="why">
  <div class="wrap">
    <h2 class="sec-title">Why Book With Us</h2>
    <div class="why-grid">
      <div class="why-item">
        <div class="why-circle blue"><svg width="80" height="80" viewBox="0 0 80 80"><rect x="14" y="10" width="52" height="60" rx="4" fill="none" stroke="#1b7cc3" stroke-width="4"/><rect x="22" y="18" width="36" height="20" fill="#1b7cc3"/><path d="M24 48h8M36 48h8M48 48h8M24 58h8M36 58h8M48 58h8" stroke="#1b7cc3" stroke-width="4"/></svg></div>
        <h4>No Deposit<br>bookings</h4>
        <p>Secure your holiday today and pay nothing up front, with the balance due shortly before you arrive.</p>
      </div>
      <div class="why-item">
        <div class="why-circle"><svg width="80" height="80" viewBox="0 0 80 80"><path d="M40 8 66 18v20c0 18-12 30-26 34C26 68 14 56 14 38V18z" fill="#8db42b"/><path d="m28 40 9 9 16-18" stroke="#fff" stroke-width="5" fill="none"/></svg></div>
        <h4>Easy Check<br>In</h4>
        <p>Collect your keys on arrival and head straight to your lodge, with our team on hand if you need help.</p>
      </div>
      <div class="why-item">
        <div class="why-circle"><svg width="80" height="80" viewBox="0 0 80 80"><rect x="18" y="10" width="44" height="60" fill="none" stroke="#8db42b" stroke-width="4"/><path d="M26 24h28M26 34h28M26 44h20" stroke="#8db42b" stroke-width="4"/><path d="m46 58 6 6 12-14" stroke="#8db42b" stroke-width="4" fill="none"/></svg></div>
        <h4>Written<br>Confirmation</h4>
        <p>Every booking is confirmed in writing, so you have all the details of your stay in one place.</p>
      </div>
      <div class="why-item">
        <div class="why-circle"><svg width="80" height="80" viewBox="0 0 80 80"><circle cx="40" cy="40" r="26" fill="none" stroke="#8db42b" stroke-width="4"/><circle cx="40" cy="34" r="8" fill="#8db42b"/><path d="M26 54a14 12 0 0 1 28 0" fill="#8db42b"/></svg></div>
        <h4>Reputable<br>Owners</h4>
        <p>All of our owners are vetted and trusted, and each holiday home is inspected before every season.</p>
      </div>
    </div>
  </div>
</section>

<section class="things">
  <div class="wrap">
    <h2 class="sec-title">Things to do Thornbeck Castle</h2>
    <div class="things-grid">
      <div class="thing"><div class="ph" style="background:linear-gradient(180deg,#3f78b8,#c98a3c)" role="img" aria-label="Outdoor pool at dusk"></div><div class="t"><h4>Swimming</h4><p>Heated indoor and outdoor pools open all day.</p></div></div>
      <div class="thing"><div class="ph" style="background:linear-gradient(180deg,#3f78b8,#c98a3c)" role="img" aria-label="Outdoor pool at dusk"></div><div class="t"><h4>Swimming</h4><p>Heated indoor and outdoor pools open all day.</p></div></div>
      <div class="thing"><div class="ph" style="background:linear-gradient(180deg,#3f78b8,#c98a3c)" role="img" aria-label="Outdoor pool at dusk"></div><div class="t"><h4>Swimming</h4><p>Heated indoor and outdoor pools open all day.</p></div></div>
      <div class="thing"><div class="ph" style="background:linear-gradient(180deg,#3f78b8,#c98a3c)" role="img" aria-label="Outdoor pool at dusk"></div><div class="t"><h4>Swimming</h4><p>Heated indoor and outdoor pools open all day.</p></div></div>
      <div class="thing"><div class="ph" style="background:linear-gradient(180deg,#3f78b8,#c98a3c)" role="img" aria-label="Outdoor pool at dusk"></div><div class="t"><h4>Swimming</h4><p>Heated indoor and outdoor pools open all day.</p></div></div>
      <div class="thing"><div class="ph" style="background:linear-gradient(180deg,#3f78b8,#c98a3c)" role="img" aria-label="Outdoor pool at dusk"></div><div class="t"><h4>Swimming</h4><p>Heated indoor and outdoor pools open all day.</p></div></div>
      <div class="thing"><div class="ph" style="background:linear-gradient(180deg,#3f78b8,#c98a3c)" role="img" aria-label="Outdoor pool at dusk"></div><div class="t"><h4>Swimming</h4><p>Heated indoor and outdoor pools open all day.</p></div></div>
      <div class="thing"><div class="ph" style="background:linear-gradient(180deg,#3f78b8,#c98a3c)" role="img" aria-label="Outdoor pool at dusk"></div><div class="t"><h4>Swimming</h4><p>Heated indoor and outdoor pools open all day.</p></div></div>
    </div>
  </div>
</section>

<footer class="site-footer">
  <div class="wrap">
    <div class="f-col news">
      <h4>Newsletter Signup</h4>
      <p>Sign up for late deals, park news and seasonal offers sent straight to your inbox.</p>
      <div class="input">Enter your Name</div>
      <div class="input">Enter your Email</div>
      <span class="subscribe">SUBSCRIBE</span>
    </div>
    <div class="f-col contact">
      <h4>Contact Information</h4>
      <p>Contact our friendly team seven days a week for help with your booking.</p>
      <ul>
        <li><svg width="14" height="14" viewBox="0 0 14 14"><path d="M3 1 5 4 4 6c1 2 2 3 4 4l2-1 3 2-1 2C6 13 1 8 1 2z" fill="#fff"/></svg>+44 0800 000 4821</li>
        <li><svg width="14" height="12"><rect x="1" y="1" width="12" height="10" fill="none" stroke="#fff"/><path d="m1 1 6 5 6-5" stroke="#fff" fill="none"/></svg>info@fernbrookstays.com</li>
      </ul>
    </div>
    <div class="f-col sitemap">
      <h4>Sitemap</h4>
      <ul>
        <li>About Us</li><li>News</li><li>Blogs</li><li>2015 Holidays</li><li>Late Deals</li><li>Local Area</li>
        <li>Contact Us</li><li>Reviews</li><li>Privacy Policy</li><li>Booking Terms</li><li>Maps</li><li>Park Guide</li>
      </ul>
    </div>
  </div>
</footer>
<div class="bottom-bar">
  <div class="wrap">
    <span>Design by Fernbrook Stays. All Rights Reserved.</span>
    <div class="social">Social Links <i></i><i></i><i></i><i></i><i></i></div>
  </div>
</div>

</body>
</html>
```